Ecommerce Website

Hello designers of Pixel Bazaar,

Today I'm requesting webpage designs for my new start up business in Toronto Canada. I have little or no experience in this field so I decided to outsource it here! My business revolves around the retail of customizable smartphone cases, as well as other objects such as mouse pads, mugs, etc.. Our main focus is smartphone cases, tablets and such. There are a few of these types of websites out already so the idea shouldn't be too foreign. I am looking for a minimalist look for my website revolving around light colours. Should convey a sense of simplistic design with elegant feel while including aspects of the business. Please see current website at brightcasewerk.ca to see how the set-up is (currently on pre-made template). Should have a similar feel to it. Also i have a post for logo design as i currently do not have one. If you can create a logo as well for my other post along with this one, gives preference to artist.

http://jobs.pixelbazaar.com/job.aspx?id=987612
Updates

The design should be transferable to the other webpages on the site. The overall look should be the same (borders, buttons, etc)

I am not sure if I'm allowed to request the page in coding as it said non-coded earlier. However it would be preferable to have the website in CSS or HTML as well as a PSD version for alterations.

Wasn't too clear about the total requirements. We are looking for a main homepage as well as a general design for the rest of our pages such as browsing catalogue page, product page, etc.. Should be a general look that can be used for multiple pages.

I have committed the payment so please do not hesitate to post designs.

To All designers.  I have attached the logo to the brief. It has multiple colors which you can choose from. The last one on the second row is the one i prefer the best however if your site can match well with any other ones, that is okay as well. 

Reason: have a few designs for selection in mind however need to get it to the final point.

Target Market(s)

Young adults ages 19 - 32

Industry/Entity Type

Retail

Requirements
Must have
• Main slider design - Main page will have a slider which displays new products or services. Please see brightcasewerk.ca for example

Note worthy - Currently we are using a service from http://www.printlumo.com/ so please make sure that it the design will work with that in mind.

```html
<!DOCTYPE html>
<html lang="en">
<head>
<meta charset="utf-8">
<title>Brightcase Werk – Create Your Own</title>
<link href="https://fonts.googleapis.com/css2?family=Open+Sans:wght@400;600;700&family=Raleway:wght@300;400;500&display=swap" rel="stylesheet">
<style>
:root{
  --green:#8db52c;
  --green-dark:#7aa021;
  --dark:#3c3c3c;
  --darker:#333333;
  --page:#e8e8e8;
  --bar:#ececec;
  --ink:#111111;
  --muted:#8a8a8a;
  --line:#d2d2d2;
  --white:#ffffff;
}
*{box-sizing:border-box;margin:0;padding:0}
html,body{width:675px;height:1200px;overflow:hidden;background:var(--page)}
body{position:relative;font-family:"Open Sans",Arial,sans-serif;color:var(--ink)}
.abs{position:absolute}

/* utility bar */
.utility-bar{left:0;top:0;width:675px;height:28px;background:var(--bar);font-size:8px;color:#222}
.utility-bar .item{position:absolute;top:9px;display:flex;align-items:center;gap:4px;white-space:nowrap}
.utility-bar .phone b{color:var(--green);font-weight:600}
.search-box{position:absolute;left:507px;top:4px;width:141px;height:18px;background:#9a9a9a;color:#fff;font-size:7px;padding:5px 8px}

/* navigation */
.main-nav{left:0;top:28px;width:675px;height:51px;background:var(--dark)}
.brand{position:absolute;left:30px;top:14px;display:flex;align-items:center;gap:5px;color:var(--green);font-size:10px;font-weight:700;line-height:1.05;width:100px}
.brand .dot{width:14px;height:14px;border-radius:50%;background:var(--green);flex:none}
.nav-divider{position:absolute;left:129px;top:10px;width:1px;height:32px;background:#555}
.nav-link{position:absolute;top:16px;color:#fff;font-size:9.5px;font-weight:600;line-height:1;white-space:nowrap}
.nav-link small{display:block;color:#9a9a9a;font-size:7px;font-weight:400;margin-top:2px}

/* hero slider */
.hero{left:0;top:79px;width:675px;height:325px;background:linear-gradient(100deg,#e9e9e7 0%,#d8d5d2 35%,#c9b8ad 55%,#e4e2e0 80%,#f0efed 100%)}
.hero-caption{position:absolute;left:73px;top:33px;width:210px;height:85px;background:var(--green);color:#fff;padding:11px 10px 0 15px;overflow:hidden}
.hero-caption h1{font-family:"Raleway",Arial,sans-serif;font-weight:400;font-size:18px;line-height:1;white-space:nowrap;letter-spacing:-0.1px}
.hero-caption h2{font-family:"Raleway",Arial,sans-serif;font-weight:400;font-size:11.5px;line-height:1.1;margin-top:2px;white-space:nowrap}
.hero-caption p{font-size:7px;margin-top:9px;line-height:1.3}
.slider-dots{position:absolute;left:63px;top:301px;display:flex;gap:5px}
.slider-dots span{width:7px;height:7px;background:var(--green)}

/* sections */
.feature{top:441px;width:200px;text-align:center}
.feature h3{font-family:"Open Sans",Arial,sans-serif;font-weight:400;font-size:12.5px;line-height:1.2;white-space:nowrap}
.feature h4{font-weight:400;font-size:8px;color:#555;margin-top:1px}
.feature svg{display:block;margin:13px auto 0}
.feature p{font-size:8px;line-height:1.45;margin-top:14px;padding:0 20px}
.divider{left:22px;width:632px;height:1px;background:var(--line)}

.product-card{top:628px;width:143px;height:121px;background:var(--dark)}
.product-card .photo{height:86px}
.product-card .label{padding:4px 0 0 12px;color:var(--green);font-size:7.5px;line-height:1.2;white-space:nowrap}
.product-card .label span{display:block;color:#fff;font-size:6.5px;font-weight:600}

.section-title{left:0;width:675px;text-align:center}
.section-title h2{font-family:"Raleway",Arial,sans-serif;font-weight:400;font-size:17px;line-height:1}
.section-title h3{font-family:"Raleway",Arial,sans-serif;font-weight:400;font-size:8px;color:var(--muted);margin-top:3px}
.about-text{left:90px;top:840px;width:495px;text-align:center;font-family:"Raleway",Arial,sans-serif;font-size:12px;line-height:1.5;color:#333}

.testimonial{top:973px;width:143px;height:69px;background:var(--white);padding:7px 14px}
.testimonial h4{color:var(--green);font-size:9.5px;font-weight:700}
.testimonial p{font-size:7px;line-height:1.35;margin-top:4px}
.testimonial .tail{position:absolute;right:14px;bottom:-9px;width:0;height:0;border-left:16px solid transparent;border-top:9px solid var(--white)}
.add-review{left:506px;top:980px;width:95px}
.add-review h4{font-family:"Raleway",Arial,sans-serif;font-weight:400;font-size:12px;white-space:nowrap}
.add-review p{font-size:6.5px;color:#333;line-height:1.3;margin-top:3px}
.add-review .btn{display:block;margin:7px 0 0 22px;width:61px;height:14px;background:var(--green);color:#fff;font-size:7px;text-align:center;line-height:14px}

/* footer */
.site-footer{left:0;top:1078px;width:675px;height:122px;background:var(--darker);color:#ddd}
.foot-col{position:absolute;top:26px;font-size:8px;line-height:11.4px;white-space:nowrap}
.foot-col h5{font-size:8px;font-weight:700;color:#fff;margin-bottom:1px}
.newsletter{position:absolute;left:368px;top:25px;font-size:8.5px;font-weight:600;color:#fff}
.social{position:absolute;left:424px;top:26px;display:flex;gap:8px}
.social span{width:9px;height:9px;border-radius:50%;background:#fff}
.field{position:absolute;top:40px;height:14px;background:#222;color:#777;font-size:6.5px;padding:3px 5px}
.join{position:absolute;left:578px;top:40px;width:47px;height:14px;background:var(--green);color:#fff;font-size:7px;text-align:center;line-height:14px}
.legal{position:absolute;right:50px;top:87px;text-align:right;font-size:6.3px;line-height:11px;color:#fff;white-space:nowrap}
.legal .dim{color:#111}
</style>
</head>
<body>

<header class="abs utility-bar">
  <div class="item" style="left:17px">
    <svg width="11" height="9" viewBox="0 0 11 9"><path d="M0 1h2l1.5 5h6L11 2H3" fill="none" stroke="#8db52c" stroke-width="1.2"/><circle cx="4" cy="8" r="0.9" fill="#8db52c"/><circle cx="9" cy="8" r="0.9" fill="#8db52c"/></svg>
    Cart: 0 items</div>
  <div class="item" style="left:97px">
    <svg width="11" height="7" viewBox="0 0 11 7"><ellipse cx="5.5" cy="3.5" rx="5" ry="3" fill="none" stroke="#8db52c" stroke-width="1.2"/><circle cx="5.5" cy="3.5" r="1.4" fill="#8db52c"/></svg>
    0 Recent items</div>
  <div class="item" style="left:183px">
    <svg width="9" height="9" viewBox="0 0 9 9"><circle cx="4.5" cy="4.5" r="3.8" fill="none" stroke="#8db52c" stroke-width="1.2"/></svg>
    Currency CAD</div>
  <div class="item phone" style="left:286px">CALL US ON <b>6475550142</b></div>
  <div class="item" style="left:415px;font-weight:600">LOG IN | REGISTER</div>
  <div class="search-box">Search</div>
  <svg class="abs" style="left:653px;top:7px" width="12" height="12" viewBox="0 0 12 12"><circle cx="5" cy="5" r="3.6" fill="none" stroke="#8db52c" stroke-width="1.8"/><path d="M7.6 7.6L11 11" stroke="#8db52c" stroke-width="2"/></svg>
</header>

<nav class="abs main-nav">
  <div class="brand"><span class="dot"></span>Brightcase Werk</div>
  <div class="nav-divider"></div>
  <div class="nav-link" style="left:170px">HOME<small>Start here</small></div>
  <div class="nav-link" style="left:238px">DESIGNS<small>Our portfolio</small></div>
  <div class="nav-link" style="left:316px">CREATE<small>Amazing things</small></div>
  <div class="nav-link" style="left:391px">ABOUT<small>Know us more</small></div>
  <div class="nav-link" style="left:463px">CONTACT<small>Get in touch</small></div>
  <div class="nav-link" style="left:545px">REQUEST A QUOTE<small>We look forward</small></div>
</nav>

<section class="abs hero" role="img" aria-label="Slide photo: a young woman in a knit hat holding up a smartphone with a custom case">
  <div class="hero-caption">
    <h1>CREATE YOUR OWN</h1>
    <h2>WE PRINT YOUR IDEAS!</h2>
    <p>CELL PHONE CASES, MOUSE PADS, MUGS<br>AND MORE!</p>
  </div>
  <svg class="abs" style="left:13px;top:126px" width="31" height="55" viewBox="0 0 31 55"><path d="M29 1L2 27.5 29 54" fill="none" stroke="#8db52c" stroke-width="2.2"/></svg>
  <svg class="abs" style="left:630px;top:126px" width="31" height="55" viewBox="0 0 31 55"><path d="M2 1l27 26.5L2 54" fill="none" stroke="#8db52c" stroke-width="2.2"/></svg>
  <div class="slider-dots"><span></span><span></span><span></span><span></span></div>
</section>

<div class="abs feature" style="left:27px">
  <h3>DESIGNING YOUR OWN</h3><h4>ANYTHING YOU CAN THINK OF</h4>
  <svg width="36" height="36" viewBox="0 0 36 36"><path d="M6 30l2-8L24 6l6 6-16 16z" fill="#000"/><path d="M6 30l2-8 6 6z" fill="#000"/><path d="M22 8l6 6" stroke="#e8e8e8" stroke-width="1.5"/></svg>
  <p>Lorem ipsum dolor sit amet, consectetur adipiscing elit. Sed at ante. Mauris eleifend, quam a vulputate dictum.</p>
</div>
<div class="abs feature" style="left:240px">
  <h3>BRIGHT IDEAS</h3><h4>ANYTHING YOU CAN THINK OF</h4>
  <svg width="36" height="36" viewBox="0 0 36 36"><path d="M18 3a11 11 0 0 0-7 19.5c1.5 1.3 2 2.5 2 4.5h10c0-2 .5-3.2 2-4.5A11 11 0 0 0 18 3z" fill="#000"/><rect x="13" y="28" width="10" height="2.5" fill="#000"/><rect x="14" y="32" width="8" height="2.5" rx="1" fill="#000"/></svg>
  <p>Lorem ipsum dolor sit amet, consectetur adipiscing elit. Sed at ante. Mauris eleifend, quam a vulputate dictum.</p>
</div>
<div class="abs feature" style="left:448px">
  <h3>100% CUSTOMIZABLE</h3><h4>ANYTHING YOU CAN THINK OF</h4>
  <svg width="36" height="36" viewBox="0 0 36 36"><g fill="#000"><circle cx="18" cy="18" r="11"/><rect x="15" y="2" width="6" height="32"/><rect x="2" y="15" width="32" height="6"/><rect x="15" y="2" width="6" height="32" transform="rotate(45 18 18)"/><rect x="15" y="2" width="6" height="32" transform="rotate(-45 18 18)"/></g><circle cx="18" cy="18" r="4.5" fill="#e8e8e8"/></svg>
  <p>Lorem ipsum dolor sit amet, consectetur adipiscing elit. Sed at ante. Mauris eleifend, quam a vulputate dictum.</p>
</div>

<div class="abs divider" style="top:597px"></div>

<article class="abs product-card" style="left:33px">
  <div class="photo" role="img" aria-label="Four phone cases in blue, red, purple and pink" style="background:linear-gradient(90deg,#2b5fc4,#c4203a 35%,#9b2fb0 65%,#e0308a)"></div>
  <div class="label">LOREM IPSUM DOLOR SIT AMET<span>Lorem ipsum dolor sit amet</span></div>
</article>
<article class="abs product-card" style="left:189px">
  <div class="photo" role="img" aria-label="Hand holding a black phone in a case" style="background:linear-gradient(90deg,#b8aea4,#3a3a3a 45%,#3a3a3a 60%,#c9c3bd)"></div>
  <div class="label">LOREM IPSUM DOLOR SIT AMET<span>Lorem ipsum dolor sit amet</span></div>
</article>
<article class="abs product-card" style="left:345px">
  <div class="photo" role="img" aria-label="Red phone cases shown from side and back" style="background:linear-gradient(90deg,#dedede,#b31a1f 30%,#d9d9d9 55%,#b31a1f 75%,#e0e0e0)"></div>
  <div class="label">LOREM IPSUM DOLOR SIT AMET<span>Lorem ipsum dolor sit amet</span></div>
</article>
<article class="abs product-card" style="left:501px">
  <div class="photo" role="img" aria-label="Woman holding a silver phone" style="background:linear-gradient(90deg,#8a6a55,#d6b8a3 45%,#eeeeee)"></div>
  <div class="label">LOREM IPSUM DOLOR SIT AMET<span>Lorem ipsum dolor sit amet</span></div>
</article>

<div class="abs divider" style="top:776px"></div>

<div class="abs section-title" style="top:798px"><h2>WHAT WE DO</h2><h3>PRINTING YOUR IDEAS</h3></div>
<p class="abs about-text">Our business revolves around the retail of customizable smartphone cases, as well as other objects such as mouse pads, mugs, etc.</p>

<div class="abs divider" style="top:902px"></div>

<div class="abs section-title" style="top:926px"><h2>TESTIMONIALS</h2><h3>WHAT ARE OUR CUSTOMERS SAYING OF US!</h3></div>

<blockquote class="abs testimonial" style="left:33px"><h4>Nora Petrak</h4><p>Nulla facilisi. Nunc volutpat. Vestibulum ante ipsum primis in faucibus orci luctus et ultrices posuere cubilia Curae.</p><span class="tail"></span></blockquote>
<blockquote class="abs testimonial" style="left:190px"><h4>Nora Petrak</h4><p>Nulla facilisi. Nunc volutpat. Vestibulum ante ipsum primis in faucibus orci luctus et ultrices posuere cubilia Curae.</p><span class="tail"></span></blockquote>
<blockquote class="abs testimonial" style="left:347px"><h4>Nora Petrak</h4><p>Nulla facilisi. Nunc volutpat. Vestibulum ante ipsum primis in faucibus orci luctus et ultrices posuere cubilia Curae.</p><span class="tail"></span></blockquote>

<div class="abs add-review">
  <h4>Add your own!</h4>
  <p>Tell us what you think of Brightcase Werk!</p>
  <span class="btn">Add Review</span>
</div>
<svg class="abs" style="left:602px;top:973px" width="47" height="75" viewBox="0 0 47 75"><rect x="1.5" y="1.5" width="44" height="72" rx="5" fill="none" stroke="#3c3c3c" stroke-width="3"/><rect x="6" y="10" width="35" height="52" fill="none" stroke="#3c3c3c" stroke-width="1.5"/><line x1="18" y1="6" x2="29" y2="6" stroke="#3c3c3c" stroke-width="1.5"/><circle cx="23.5" cy="68" r="2" fill="#3c3c3c"/><path d="M16 46l1.5-5 10-10 3.5 3.5-10 10z" fill="#3c3c3c"/></svg>

<footer class="abs site-footer">
  <div class="foot-col" style="left:45px"><h5>Site Links</h5>Home<br>Create<br>About<br>Contact<br>Request a Quote</div>
  <div class="foot-col" style="left:135px"><h5>Need Help</h5>Product sizes<br>How to use online designer<br>Returns Policy<br>Guarantee<br>Shipping information<br>Where is my order?</div>
  <div class="foot-col" style="left:264px"><h5>About Us</h5>About Us<br>Feedback<br>Privacy Policy<br>User Agreement<br>Sublimation Information</div>
  <div class="newsletter">Newsletter</div>
  <div class="social" aria-label="Social links"><span></span><span></span><span></span></div>
  <div class="field" style="left:368px;width:100px">Email</div>
  <div class="field" style="left:474px;width:99px">Name</div>
  <div class="join">Join</div>
  <div class="legal"><span class="dim">User agreement</span> and Privacy and <span class="dim">cookie policy</span><br>Copyright 2013, Brightcase Werk All rights reserved.</div>
</footer>

</body>
</html>
```